Redesign of WordHarbor.com in Bootstrap 4

Current design of WordHarbor.com is not responsive. We need to change it to latest version of Bootstrap 4 keeping essential elements in place.

Apart from home page, we need designs for http://www.wordharbor.com/meaning/cat also.

Coding

Coded - Design and coding required

Number of Pages Required

2 page

Colors
34a7d8

Requirements
Must have
• Bootstrap 4

```html
<!DOCTYPE html>
<html lang="en">
<head>
<meta charset="utf-8">
<title>WordHarbor – Search, Save and Master Words</title>
<link href="https://fonts.googleapis.com/css2?family=Open+Sans:wght@400;600;700;800&display=swap" rel="stylesheet">
<style>
:root{
  --blue:#34a7d8;
  --blue-dark:#2a8fbb;
  --ink:#333333;
  --band:#333333;
  --orange:#f7941d;
  --muted:#555555;
  --line:#e5e5e5;
  --white:#ffffff;
}
*{box-sizing:border-box;margin:0;padding:0}
html,body{width:1079px;height:1200px;overflow:hidden;background:var(--white)}
body{position:relative;font-family:'Open Sans',Arial,sans-serif;color:var(--ink)}
.abs{position:absolute}
/* header */
.brand{left:145px;top:24px;font-weight:800;font-size:19px;color:var(--orange);letter-spacing:-.3px}
.main-nav{left:0;top:36px;width:100%;height:14px;font-size:9px;color:#444}
.main-nav span{position:absolute;white-space:nowrap}
.main-nav .active{color:var(--blue)}
.login-btn{left:818px;top:26px;width:116px;height:33px;border-radius:17px;background:var(--blue);box-shadow:0 0 0 2px #cfe8f3;color:var(--white);font-size:9px;display:flex;align-items:center;justify-content:center}
/* browse bar */
.browse{left:0;top:82px;width:1079px;height:41px;background:var(--band)}
.browse-title{left:164px;top:11px;color:var(--white);font-weight:700;font-size:16px}
.letters{left:373px;top:13px;display:flex;font-weight:700;font-size:11.5px;color:var(--white)}
.letters span{width:21.3px}
.letters .current{color:var(--orange)}
/* hero */
.hero{left:0;top:123px;width:1079px;height:364px;background:var(--blue)}
.hero-title{left:0;top:181px;width:1079px;text-align:center;font-weight:700;font-size:32px;color:var(--ink)}
.search-frame{left:206px;top:247px;width:667px;height:62px;border-radius:6px;background:var(--blue-dark)}
.search-field{left:212px;top:253px;width:654px;height:49px;background:var(--white)}
.search-placeholder{left:272px;top:272px;font-size:12px;color:#bbb}
.search-btn{left:766px;top:256px;width:97px;height:43px;background:var(--orange);color:var(--white);font-weight:600;font-size:12px;display:flex;align-items:center;justify-content:center}
.example{left:213px;top:318px;font-size:9.5px;color:var(--ink)}
.perk{font-size:11px;color:var(--white);line-height:16px;width:290px}
.tick{width:12px;height:12px}
/* word of the day */
.wotd{left:0;top:487px;width:1079px;height:77px;background:var(--band)}
.wotd-label{left:155px;top:511px;font-weight:800;font-size:19px;line-height:16.5px;color:var(--orange)}
.wotd-word{left:293px;top:514px;font-weight:700;font-size:17.5px;color:var(--white)}
.wotd-def{left:425px;top:522px;font-size:9.5px;color:var(--white)}
.btn-orange{background:var(--orange);color:var(--white);font-weight:700;font-size:9px;display:flex;align-items:center;justify-content:center}
/* features */
.divider{top:590px;width:1px;height:247px;background:#eeeeee}
.feature-title{font-weight:600;font-size:16px;line-height:20px;color:var(--blue)}
.feature-sub{top:697px;font-weight:600;font-size:12px;color:var(--ink)}
.feature-body{font-size:9.5px;line-height:16px;color:var(--muted)}
.btn-line{height:30px;border:1px solid var(--blue);color:var(--blue);font-weight:600;font-size:9.5px;display:flex;align-items:center;justify-content:center}
.btn-fill{height:30px;background:var(--blue);color:var(--white);font-weight:600;font-size:9.5px;display:flex;align-items:center;justify-content:center}
/* newsletter */
.newsletter{left:0;top:884px;width:1079px;height:99px;background:var(--band)}
.news-title{left:146px;top:913px;font-weight:700;font-size:12px;color:var(--white)}
.news-sub{left:146px;top:936px;font-size:9.5px;color:var(--white)}
.news-input{left:416px;top:915px;width:383px;height:33px;background:var(--white);font-size:9.5px;color:#666;padding-left:12px;display:flex;align-items:center}
/* footer */
.foot-brand{left:156px;top:1050px;font-weight:800;font-size:19px;color:var(--orange);letter-spacing:-.3px}
.foot-col{width:140px}
.foot-col h4{font-weight:600;font-size:12px;color:#444;margin-bottom:8px}
.foot-col a{display:block;font-size:9.5px;color:#555;text-decoration:none;padding:0 0 6px 7px;margin-bottom:7px;border-bottom:1px solid var(--line);line-height:11px}
.bottom-bar{left:0;top:1152px;width:1079px;height:48px;background:var(--blue)}
.copyright{left:145px;top:1171px;font-size:9.5px;color:var(--white)}
.social{top:1173px;width:10px;height:10px;border-radius:50%;background:var(--white)}
</style>
</head>
<body>

<header>
  <div class="abs brand">WordHarbor</div>
  <nav class="abs main-nav">
    <span class="active" style="left:402px">HOME</span>
    <span style="left:457px">IDIOMS</span>
    <span style="left:517px">COMMON ERRORS</span>
    <span style="left:624px">CROSSWORD</span>
    <span style="left:705px">BLOG</span>
    <span style="left:750px">CONTACT</span>
  </nav>
  <div class="abs login-btn">LOGIN / REGISTER</div>
</header>

<section class="abs browse">
  <div class="abs browse-title">BROWSE DICTIONARY</div>
  <div class="abs letters">
    <span>A</span><span>B</span><span>C</span><span class="current">D</span><span>E</span><span>F</span><span>G</span><span>H</span><span>I</span><span>J</span><span>K</span><span>L</span><span>M</span><span>N</span><span>O</span><span>P</span><span>Q</span><span>R</span><span>S</span><span>T</span><span>U</span><span>V</span><span>W</span><span>X</span><span>Y</span><span>Z</span>
  </div>
</section>

<section class="abs hero" role="img" aria-label="Blue backdrop with faint scattered vocabulary words"></section>
<h1 class="abs hero-title">SEARCH, SAVE AND MASTER WORDS</h1>
<div class="abs search-frame"></div>
<div class="abs search-field"></div>
<svg class="abs" style="left:223px;top:261px" width="32" height="32" viewBox="0 0 32 32"><circle cx="13" cy="13" r="9.5" fill="none" stroke="#c8c8c8" stroke-width="4"/><line x1="20" y1="20" x2="29" y2="29" stroke="#c8c8c8" stroke-width="5" stroke-linecap="round"/></svg>
<div class="abs search-placeholder">Enter a word or phrase</div>
<div class="abs search-btn">SEARCH</div>
<div class="abs example">(eg. origin, sign, butterfly)</div>

<svg width="0" height="0" style="position:absolute"><defs><path id="tick" d="M1 6.5 L4.5 10 L11 1.5" fill="none" stroke="#333" stroke-width="2.4"/></defs></svg>
<svg class="abs tick" style="left:214px;top:349px" viewBox="0 0 12 12"><use href="#tick"/></svg>
<div class="abs perk" style="left:241px;top:345px">Search from more than 300,000 words and phrases</div>
<svg class="abs tick" style="left:214px;top:376px" viewBox="0 0 12 12"><use href="#tick"/></svg>
<div class="abs perk" style="left:241px;top:372px">Multiple usages to clarify the context</div>
<svg class="abs tick" style="left:214px;top:400px" viewBox="0 0 12 12"><use href="#tick"/></svg>
<div class="abs perk" style="left:241px;top:398px;width:300px">Audio, phonetics, meanings, synonyms and antonyms</div>
<svg class="abs tick" style="left:553px;top:349px" viewBox="0 0 12 12"><use href="#tick"/></svg>
<div class="abs perk" style="left:576px;top:345px;width:300px">Save the words to your personal deck and access from anywhere</div>
<svg class="abs tick" style="left:553px;top:399px" viewBox="0 0 12 12"><use href="#tick"/></svg>
<div class="abs perk" style="left:576px;top:398px">It’s FREE</div>

<section class="abs wotd"></section>
<div class="abs wotd-label">WORD OF<br>THE DAY</div>
<div class="abs wotd-word">affluent</div>
<svg class="abs" style="left:369px;top:518px" width="18" height="18" viewBox="0 0 18 18"><circle cx="9" cy="9" r="9" fill="#fff"/><path d="M5.5 7.5h2l2.5-2v7l-2.5-2h-2z" fill="#34a7d8"/></svg>
<div class="abs wotd-def">/ˈæ flu ənt /&nbsp; (s) having an abundant supply of money or possessions of value</div>
<div class="abs btn-orange" style="left:819px;top:512px;width:114px;height:30px">MORE INFO</div>

<div class="abs divider" style="left:341px"></div>
<div class="abs divider" style="left:541px"></div>
<div class="abs divider" style="left:735px"></div>

<svg class="abs" style="left:165px;top:638px" width="38" height="38" viewBox="0 0 38 38"><rect x="2" y="5" width="28" height="31" rx="3" fill="none" stroke="#ccc" stroke-width="2.5"/><rect x="29" y="1" width="7" height="7" fill="#ccc"/><circle cx="16" cy="14" r="2" fill="#ccc"/><rect x="14" y="18" width="4" height="11" fill="#ccc"/></svg>
<div class="abs feature-title" style="left:213px;top:639px">ENGLISH<br>TIDBIT</div>
<div class="abs feature-sub" style="left:165px">mediator/interlocutor</div>
<p class="abs feature-body" style="left:164px;top:722px;width:165px">A mediator is a negotiator who acts as a link between parties while a interlocutor is a person who takes part in a conversation.</p>

<svg class="abs" style="left:359px;top:639px" width="36" height="36" viewBox="0 0 36 36"><rect width="36" height="36" fill="#d4d4d4"/><g fill="#fff"><rect x="1" y="1" width="6" height="6"/><rect x="15" y="1" width="6" height="6"/><rect x="29" y="8" width="6" height="6"/><rect x="8" y="15" width="6" height="6"/><rect x="22" y="15" width="6" height="6"/><rect x="1" y="22" width="6" height="6"/><rect x="15" y="29" width="6" height="6"/><rect x="29" y="29" width="6" height="6"/><rect x="22" y="1" width="6" height="6"/><rect x="8" y="29" width="6" height="6"/></g></svg>
<div class="abs feature-title" style="left:409px;top:639px">DAILY<br>CROSSWORD</div>
<div class="abs feature-sub" style="left:361px">Crossword Lovers</div>
<p class="abs feature-body" style="left:361px;top:722px;width:150px">Take this daily crossword challenge from WordHarbor.</p>
<div class="abs btn-line" style="left:362px;top:780px;width:75px">Solve now</div>

<svg class="abs" style="left:559px;top:639px" width="38" height="36" viewBox="0 0 38 36"><rect x="0" y="0" width="16" height="16" fill="#ccc"/><rect x="0" y="18" width="16" height="16" fill="#d8d8d8"/><rect x="18" y="0" width="14" height="16" fill="#d8d8d8"/><rect x="20" y="18" width="16" height="16" fill="#c4c4c4"/></svg>
<div class="abs feature-title" style="left:617px;top:639px">EMBERFOX<br>ADDON</div>
<p class="abs feature-body" style="left:559px;top:697px;width:170px">Add this tool to your Emberfox and quickly look up for definitions from any website without leaving the page.</p>
<div class="abs btn-fill" style="left:559px;top:780px;width:75px">Get it now</div>

<svg class="abs" style="left:755px;top:639px" width="20" height="37" viewBox="0 0 20 37"><rect x="1.5" y="1.5" width="17" height="34" rx="3" fill="none" stroke="#ccc" stroke-width="2.5"/><rect x="4" y="7" width="12" height="20" fill="#ccc"/><circle cx="10" cy="31" r="1.8" fill="#ccc"/></svg>
<div class="abs feature-title" style="left:788px;top:639px">DESIGNED FOR<br>UPHONE</div>
<p class="abs feature-body" style="left:754px;top:697px;width:170px">WordHarbor is specially designed for your uPhone to quickly lookup meaining, usages and audio of words.</p>
<div class="abs btn-line" style="left:752px;top:780px;width:97px">Download now</div>

<section class="abs newsletter"></section>
<div class="abs news-title">NEWSLETTER SUBSCRIPTION</div>
<div class="abs news-sub">Learn a new word every day. Direct into your inbox!</div>
<div class="abs news-input">Enter your email address</div>
<div class="abs btn-orange" style="left:819px;top:915px;width:114px;height:33px">SUBSCRIBE</div>

<footer>
  <div class="abs foot-brand">WordHarbor</div>
  <div class="abs foot-col" style="left:348px;top:1018px">
    <h4>WordHarbor.com</h4>
    <a>Faq</a><a>Contact</a><a>Blog</a>
  </div>
  <div class="abs foot-col" style="left:550px;top:1018px">
    <h4>Others</h4>
    <a>Popular Words</a><a>Common Errors in English</a><a>Exam Prep Online</a>
  </div>
  <div class="abs foot-col" style="left:753px;top:1018px">
    <h4>Legal</h4>
    <a>Privacy Policy</a><a>Terms of Use</a>
  </div>
  <div class="abs bottom-bar"></div>
  <div class="abs copyright">© 2016 WordHarbor.com. All rights reserved.</div>
  <div class="abs social" style="left:871px" role="img" aria-label="Social network link"></div>
  <div class="abs social" style="left:893px" role="img" aria-label="Social network link"></div>
  <div class="abs social" style="left:917px" role="img" aria-label="Social network link"></div>
</footer>

</body>
</html>
```